Flyer-Design für nachhaltige Spülbecher aus Keramik
Zielgruppe
Zielgruppe des Flyers sind Zahnärzte. Wir fertigen die ersten nachhaltigen Spülbecher für Praxen aus Keramik.
Aufgabenstellung
Der Flyer soll einen hochwertigen und exklusiven Eindruck hinterlassen.
Auf dem Flyer sollte das Logo, Kontaktmöglichkeiten, Anschrift, 1-2 Bilder des Produktes und ein kleiner Text bezüglich Nachhaltigkeit vorhanden sein. Die aktuell hochgeladenen Bilder der Becher sind aktuell noch Platzhalter, es werden in den nächsten Tagen die richtigen Bilder hochgeladen.
WICHTIG: Bitte einen Platzhalter für eine Überschrift und Stichpunkte/Informationen einarbeiten. Leider ist noch nicht Final klar wir diese Lauten soll, daher wird dieser Teil noch von mir noch selbst ergänzt. Danke
Website: www.lindgau-keramik.de

```html
<!DOCTYPE html>
<html lang="de">
<head>
<meta charset="utf-8">
<title>Lindgau Keramik – Flyer</title>
<link href="https://fonts.googleapis.com/css2?family=Montserrat:wght@500&family=Open+Sans:wght@400;700&family=Source+Serif+4:wght@500&display=swap" rel="stylesheet">
<style>
  :root{
    --stage:#cccccc;
    --ink:#231f20;
    --paper:#ffffff;
    --text:#2b2b2b;
    --muted:#444444;
  }
  *{margin:0;padding:0;box-sizing:border-box}
  html,body{width:1200px;height:894px;overflow:hidden;background:var(--stage)}
  .canvas{position:relative;width:1200px;height:894px}
  .page{position:absolute;width:588px;overflow:hidden}
  .page--cover{left:12px;top:39px;height:834px;background:var(--ink)}
  .page--products{left:605px;top:35px;height:838px;background:var(--paper)}
  .cover__photo{position:absolute;left:0;top:0;width:588px;height:475px;
    background:
      radial-gradient(ellipse 90px 130px at 120px 300px,#b1706a 0%,rgba(177,112,106,0) 100%),
      radial-gradient(ellipse 90px 140px at 230px 280px,#d8dfdc 0%,rgba(216,223,220,0) 100%),
      radial-gradient(ellipse 100px 150px at 370px 320px,#e9e8e6 0%,rgba(233,232,230,0) 100%),
      radial-gradient(ellipse 90px 80px at 90px 160px,#a9cde8 0%,rgba(169,205,232,0) 100%),
      radial-gradient(ellipse 90px 80px at 270px 110px,#3f88b4 0%,rgba(63,136,180,0) 100%),
      radial-gradient(ellipse 90px 80px at 400px 70px,#94b454 0%,rgba(148,180,84,0) 100%),
      radial-gradient(ellipse 90px 80px at 480px 170px,#8e8e95 0%,rgba(142,142,149,0) 100%),
      #141414}
  .page svg.shapes{position:absolute;left:0;top:0}
  .logo{position:absolute;left:0;width:100%;display:flex;justify-content:center;align-items:center;gap:12px;
    font-family:"Montserrat",sans-serif;font-weight:500;color:var(--paper)}
  .logo__square{border:2px solid var(--paper)}
  .brand__name{position:absolute;left:0;width:100%;text-align:center;font-family:"Montserrat",sans-serif;font-weight:500;font-size:21px;color:var(--paper)}
  .contact{position:absolute;left:0;width:100%;text-align:center;color:var(--paper);font-family:"Open Sans",sans-serif}
  .contact__company{font-weight:700;font-size:14px;line-height:16px}
  .contact__address{font-size:13px;line-height:16px}
  .contact__line{display:flex;justify-content:center;align-items:center;gap:12px}
  .contact__line svg{flex:none}
  .contact__phone{font-size:21px;margin-top:6px}
  .contact__mail,.contact__web{font-size:14px;margin-top:8px}
  .product__photo{position:absolute}
  .product__text{position:absolute;width:142px;font-family:"Open Sans",sans-serif;color:var(--text)}
  .product__title{font-family:"Source Serif 4",serif;font-weight:500;font-size:22px;line-height:26px;color:var(--ink);margin-bottom:12px;white-space:nowrap}
  .product__copy{font-size:10px;line-height:13.5px;color:var(--muted)}
  .product__copy--wide{font-size:11px;line-height:13.5px;width:130px}
  .product__price{font-weight:700;font-size:17px;margin-top:10px;color:var(--ink)}
</style>
</head>
<body>
<div class="canvas">

  <section class="page page--cover">
    <div class="cover__photo" role="img" aria-label="Foto: sieben farbige Keramik-Spülbecher auf schwarzem Grund"></div>
    <svg class="shapes" width="588" height="834" viewBox="0 0 588 834">
      <path fill="var(--ink)" d="M0,435 L3,435 L114,470 L168,441 L246,424 L324,435 L378,471 L450,462 L528,441 L588,420 V834 H0 Z"/>
      <path fill="none" stroke="#fff" stroke-width="4" stroke-linejoin="round"
            d="M3,435 L114,470 L168,441 L246,424 L324,435 L378,471 L450,462 L528,441 L588,420"/>
    </svg>
    <div class="logo" style="top:536px;font-size:24px">
      <span class="logo__square" style="width:30px;height:30px"></span>
      <span>Lindgau</span>
    </div>
    <div class="brand__name" style="top:617px">Lindgau Keramik GmbH</div>
    <div class="contact" style="top:680px">
      <div class="contact__company">Lindgau Keramik GmbH</div>
      <div class="contact__address">Talweg 12.96231 Lindgau</div>
      <div class="contact__line contact__phone">
        <svg width="16" height="16" viewBox="0 0 24 24" fill="#fff"><path d="M6.6 10.8a15 15 0 0 0 6.6 6.6l2.2-2.2a1 1 0 0 1 1-.25 11.4 11.4 0 0 0 3.6.57 1 1 0 0 1 1 1V20a1 1 0 0 1-1 1A17 17 0 0 1 3 4a1 1 0 0 1 1-1h3.5a1 1 0 0 1 1 1c0 1.25.2 2.45.57 3.57a1 1 0 0 1-.25 1z"/></svg>
        <span>0176 / 20481736</span>
      </div>
      <div class="contact__line contact__mail">
        <svg width="14" height="10" viewBox="0 0 14 10" fill="none" stroke="#fff" stroke-width="1.2"><rect x="0.6" y="0.6" width="12.8" height="8.8"/><path d="M0.6,0.6 L7,5.5 L13.4,0.6"/></svg>
        <span>info@lindgau-keramik.de</span>
      </div>
      <div class="contact__line contact__web">
        <svg width="13" height="13" viewBox="0 0 14 14" fill="none" stroke="#fff" stroke-width="1"><circle cx="7" cy="7" r="6"/><ellipse cx="7" cy="7" rx="2.6" ry="6"/><path d="M1,7 H13 M2,4 H12 M2,10 H12"/></svg>
        <span>www.lindgau-keramik.de</span>
      </div>
    </div>
  </section>

  <section class="page page--products">
    <svg class="shapes" width="588" height="838" viewBox="0 0 588 838">
      <defs>
        <radialGradient id="blueCup" cx="0.45" cy="0.5" r="0.6"><stop offset="0" stop-color="#2f84ad"/><stop offset="0.35" stop-color="#4a8fb2"/><stop offset="0.7" stop-color="#9aa4ad"/><stop offset="1" stop-color="#e4e3df"/></radialGradient>
        <radialGradient id="greyCup" cx="0.45" cy="0.55" r="0.6"><stop offset="0" stop-color="#65676e"/><stop offset="0.4" stop-color="#76787e"/><stop offset="0.75" stop-color="#a9abaf"/><stop offset="1" stop-color="#e4e3df"/></radialGradient>
        <radialGradient id="greenCup" cx="0.45" cy="0.55" r="0.6"><stop offset="0" stop-color="#8cb044"/><stop offset="0.4" stop-color="#93ae58"/><stop offset="0.75" stop-color="#a6a9ad"/><stop offset="1" stop-color="#e4e3df"/></radialGradient>
        <radialGradient id="redCup" cx="0.45" cy="0.55" r="0.6"><stop offset="0" stop-color="#9a4f42"/><stop offset="0.4" stop-color="#9c5e52"/><stop offset="0.75" stop-color="#a3a4a8"/><stop offset="1" stop-color="#e4e3df"/></radialGradient>
      </defs>
      <rect role="img" aria-label="Foto: blauer Spülbecher unter dem Auslauf einer Behandlungseinheit" x="35" y="38" width="103" height="176" fill="url(#blueCup)"/>
      <rect role="img" aria-label="Foto: grauer Spülbecher unter dem Auslauf einer Behandlungseinheit" x="301" y="45" width="97" height="163" fill="url(#greyCup)"/>
      <rect role="img" aria-label="Foto: grüner Spülbecher unter dem Auslauf einer Behandlungseinheit" x="29" y="328" width="106" height="181" fill="url(#greenCup)"/>
      <rect role="img" aria-label="Foto: roter Spülbecher unter dem Auslauf einer Behandlungseinheit" x="299" y="324" width="101" height="175" fill="url(#redCup)"/>
      <path fill="var(--ink)" d="M0,541 L55,547 L115,572 L151,559 L241,529 L295,544 L355,565 L415,556 L505,545 L588,526 V838 H0 Z"/>
    </svg>

    <div class="product__text" style="left:150px;top:82px">
      <div class="product__title">Lorem ipsum</div>
      <div class="product__copy product__copy--wide">Lorem ipsum dolor sit amet, graecequidam&shy;eoste, facetediceretvitu&shy;peratoribusest at.</div>
      <div class="product__price">€ 39.95</div>
    </div>
    <div class="product__text" style="left:413px;top:83px">
      <div class="product__title">Lorem ipsum</div>
      <div class="product__copy">Lorem ipsum dolor sit amet, graecequidameoste, facetediceretvituperatori&shy;busest at.</div>
      <div class="product__price">€ 39.95</div>
    </div>
    <div class="product__text" style="left:150px;top:372px">
      <div class="product__title">Lorem ipsum</div>
      <div class="product__copy">Lorem ipsum dolor sit amet, graecequidameoste, facetediceretvituperatori&shy;busest at.</div>
      <div class="product__price">€ 39.95</div>
    </div>
    <div class="product__text" style="left:418px;top:370px">
      <div class="product__title">Lorem ipsum</div>
      <div class="product__copy">Lorem ipsum dolor sit amet, graecequidameoste, facetediceretvituperatori&shy;busest at.</div>
      <div class="product__price">€ 39.95</div>
    </div>

    <div class="logo" style="top:594px;font-size:21px">
      <span class="logo__square" style="width:26px;height:26px"></span>
      <span>Lindgau</span>
    </div>
    <div class="brand__name" style="top:661px;font-size:19px">Lindgau Keramik GmbH</div>
    <div class="contact" style="top:698px">
      <div class="contact__company">Lindgau Keramik GmbH</div>
      <div class="contact__address">Talweg 12.96231 Lindgau</div>
      <div class="contact__line contact__phone" style="margin-top:2px">
        <svg width="16" height="16" viewBox="0 0 24 24" fill="#fff"><path d="M6.6 10.8a15 15 0 0 0 6.6 6.6l2.2-2.2a1 1 0 0 1 1-.25 11.4 11.4 0 0 0 3.6.57 1 1 0 0 1 1 1V20a1 1 0 0 1-1 1A17 17 0 0 1 3 4a1 1 0 0 1 1-1h3.5a1 1 0 0 1 1 1c0 1.25.2 2.45.57 3.57a1 1 0 0 1-.25 1z"/></svg>
        <span>0176 / 20481736</span>
      </div>
      <div class="contact__line contact__mail" style="margin-top:6px">
        <svg width="16" height="12" viewBox="0 0 14 10" fill="none" stroke="#fff" stroke-width="1.2"><rect x="0.6" y="0.6" width="12.8" height="8.8"/><path d="M0.6,0.6 L7,5.5 L13.4,0.6"/></svg>
        <span>info@lindgau-keramik.de</span>
      </div>
      <div class="contact__line contact__web" style="margin-top:8px">
        <svg width="15" height="15" viewBox="0 0 14 14" fill="none" stroke="#fff" stroke-width="1"><circle cx="7" cy="7" r="6"/><ellipse cx="7" cy="7" rx="2.6" ry="6"/><path d="M1,7 H13 M2,4 H12 M2,10 H12"/></svg>
        <span>www.lindgau-keramik.de</span>
      </div>
    </div>
  </section>

</div>
</body>
</html>
```